Pelvo BUSINESS CARD

Design an attention-grabbing business cards. Draw inspiration from the provided logo file. Please use the same font style as in the logo.
the back side of the card is for accent/decoration.

Contact Information for Business Card

PLEASE USE PROVIDED BUSINESS CARD SAMPLE

Other font styles liked:
• MIRVALLE

Colors
EB3D1F
EC4F4E
F09395
F8D3D4
FCEDEE

Requirements
Must have
• RED, BLACK COLORS, SOLID BACK COLOR
Nice to have
• MAKE IT FANCY

```html
<!DOCTYPE html>
<html lang="en">
<head>
<meta charset="utf-8">
<title>Pelvo Business Card</title>
<link rel="stylesheet" href="https://fonts.googleapis.com/css2?family=Mulish:wght@400;600;700;800&display=swap">
<style>
  :root {
    --bg: #d4d5d7;
    --red: #dc2430;
    --red-deep: #c51d29;
    --red-tone: #b91a26;
    --black: #221f20;
    --white: #ffffff;
  }
  * { margin: 0; padding: 0; box-sizing: border-box; }
  html, body { width: 900px; height: 1200px; overflow: hidden; }
  body {
    background: var(--bg);
    font-family: "Mulish", sans-serif;
    position: relative;
  }
  .card {
    position: absolute;
    border-radius: 14px;
    overflow: hidden;
  }
  /* Front */
  .card-front {
    left: 124px; top: 191px; width: 654px; height: 373px;
    background: var(--red);
  }
  .brand-square {
    position: absolute;
    left: 55px; top: 135px; width: 107px; height: 107px;
    background: var(--red-deep);
  }
  .brand-name {
    position: absolute;
    left: 180px; top: 126px;
    font-size: 92px; font-weight: 800; letter-spacing: 28px;
    line-height: 1;
    color: var(--red-deep);
  }
  .brand-tagline {
    position: absolute;
    left: 183px; top: 226px;
    font-size: 14px; font-weight: 400; letter-spacing: 2px;
    color: var(--red-tone);
  }
  /* Back */
  .card-back {
    left: 123px; top: 622px; width: 656px; height: 375px;
    background: var(--white);
  }
  .back-shapes { position: absolute; inset: 0; width: 100%; height: 100%; }
  .contact { position: absolute; left: 43px; top: 0; color: var(--white); }
  .contact-name {
    position: absolute; top: 45px; white-space: nowrap;
    font-size: 30px; font-weight: 600; color: var(--red);
  }
  .contact-role { position: absolute; top: 82px; font-size: 17px; font-weight: 400; white-space: nowrap; }
  .contact-address {
    position: absolute; top: 147px; white-space: nowrap;
    font-size: 17.5px; line-height: 26px;
  }
  .contact-lines { position: absolute; top: 227px; list-style: none; white-space: nowrap; }
  .contact-lines li {
    display: flex; align-items: center; gap: 6px;
    font-size: 17.5px; height: 27px;
  }
  .contact-lines .spaced { letter-spacing: 4px; }
  .contact-lines svg { width: 16px; height: 16px; fill: var(--red); flex: none; }
  .back-mark {
    position: absolute; left: 447px; top: 75px;
    width: 150px; height: 150px; border-radius: 50%;
    background: var(--red);
  }
  .back-name {
    position: absolute; left: 422px; top: 248px; width: 200px;
    text-align: center;
    font-size: 30px; font-weight: 800; letter-spacing: 4px;
    color: var(--red);
  }
</style>
</head>
<body>

<section class="card card-front" aria-label="Card front">
  <div class="brand-square"></div>
  <div class="brand-name">PELVO</div>
  <div class="brand-tagline">FREIGHT MADE SIMPLE</div>
</section>

<section class="card card-back" aria-label="Card back">
  <svg class="back-shapes" viewBox="0 0 875 500" preserveAspectRatio="none">
    <path d="M350 0 H453 C515 110 532 220 514 300 C496 390 445 450 384 500 H340 Z" fill="var(--red)"/>
    <path d="M0 0 H360 C440 90 480 200 461 300 C450 380 420 440 384 500 H0 Z" fill="var(--black)" stroke="var(--white)" stroke-width="3"/>
  </svg>

  <div class="contact">
    <div class="contact-name">Dean Holloway</div>
    <div class="contact-role">President</div>
    <div class="contact-address">1480 S. 250 East.<br>Maplewood, IN, 46199</div>
    <ul class="contact-lines">
      <li class="spaced"><svg viewBox="0 0 24 24"><path d="M6.6 10.8a15 15 0 0 0 6.6 6.6l2.2-2.2c.3-.3.7-.4 1-.2 1.1.4 2.3.6 3.6.6.6 0 1 .4 1 1V20c0 .6-.4 1-1 1A17 17 0 0 1 3 4c0-.6.4-1 1-1h3.5c.6 0 1 .4 1 1 0 1.3.2 2.5.6 3.6.1.3 0 .7-.2 1z"/></svg>+317-555-0142</li>
      <li class="spaced"><svg viewBox="0 0 24 24"><path d="M7 1h10a2 2 0 0 1 2 2v18a2 2 0 0 1-2 2H7a2 2 0 0 1-2-2V3a2 2 0 0 1 2-2zm0 3v14h10V4zm5 15.5a1 1 0 1 0 0 2 1 1 0 0 0 0-2z"/></svg>+317-555-0187</li>
      <li><svg viewBox="0 0 24 24"><path d="M2 5h20v14H2zm2 2v.5l8 5 8-5V7l-8 5z"/></svg>DHolloway@pelvo-llc.com</li>
      <li><svg viewBox="0 0 24 24"><path d="M12 2a10 10 0 1 0 0 20 10 10 0 0 0 0-20zm6.9 9h-3a15 15 0 0 0-1.3-6.1A8 8 0 0 1 18.9 11zM12 4c.9 1.3 1.8 3.8 1.9 7h-3.8c.1-3.2 1-5.7 1.9-7zM9.4 4.9A15 15 0 0 0 8.1 11h-3a8 8 0 0 1 4.3-6.1zM5.1 13h3a15 15 0 0 0 1.3 6.1A8 8 0 0 1 5.1 13zM12 20c-.9-1.300-1.8-3.8-1.9-7h3.8c-.1 3.2-1 5.7-1.9 7zm2.6-.9a15 15 0 0 0 1.3-6.1h3a8 8 0 0 1-4.3 6.1z"/></svg>www.Pelvo-LLC.com</li>
    </ul>
  </div>

  <div class="back-mark"></div>
  <div class="back-name">PELVO</div>
</section>

</body>
</html>
```